Spanish Student Needs a Cover for his PhD Dissertation

Hi everyone :) So, I'm a Corneal surgeon currently finishing my PhD, with a dissertation focused on the evaluation of quality of life in patients affected by a disease called Keratoconus. Just so you know, Keratoconus is a condition in which the cornea (the frontal part of the way) gets thin and bulgy and it decreases vision. What I did during my PhD was designing a questionnaire for evaluating quality of life in this kind of patients.
I need to design a hard cover for my dissertation, which is 200 sheets long. I like kind of minimalistic and geometric designs but I am totally open to suggestions. What needs to be in the cover is the name of the dissertation "Diseño, desarrollo y validación de una encuesta para evaluar el compromiso visual y emocional subjetivos en pacientes con Queratocono" and my name, "Iñigo Tarrasco". The other thing that needs to go there is the logo of my university (Universidad de Montebrisa). Aside from that, anything else is up to the designer. It would be important to use the kind of "red" color I am using in the dissertation. I am attaching the frontal page of my dissertation so you know what kind of design and colors I am using.
In the back part, of the cover, there should be this small inscription: "Iñigo Tarrasco, MD, es un Oftalmólogo Subespecialista en Cirugía Refractiva de la Universidad Serrana Metropolitana (Colombia) y la Universidad de Montebrisa (España). Actualmente se desempeña como miembro del Departamento de Córnea y Cirugía Refractiva de la Clínica de Oftalmología Vallealto y como director de su propia compañía de emprendimiento médico Silver Heron Surgical". Please leave a space to place my picture; I will have it taken this week so I don't have it right now, you can just leave the blank spot and I will include it later
The size of the pages is standard "letter" size.
Thanks a lot!

Target Market(s)

PhD Scholars

Font styles to use
Serif

Requirements
Must have
• The "red" color I use on my font. It must be formal but "young".
Nice to have
• I like to keep the design clean, kind of "formal with a young" touch so to speak. I really like gray colors, so it would be nice to have broad areas of gray. I love geometrical designs.
I have uploaded a very early version a friend of mine made (it even had a different title); this can be a starting point for you to work on, but I am more than open to suggestions and new ideas.
Should not have
• Please don't use my whole name, Iñigo Tarrasco is fine. I don't like ALL CAPITALS.

```html
<!DOCTYPE html>
<html lang="es">
<head>
<meta charset="utf-8">
<title>Cubierta de tesis doctoral — Iñigo Tarrasco</title>
<link rel="stylesheet" href="https://fonts.googleapis.com/css2?family=Questrial&family=Roboto:wght@700&display=swap">
<style>
  :root {
    --paper: #ffffff;
    --slate: #646a61;
    --crimson: #a51d3d;
    --ink: #1a1a1a;
    --photo-dark: #5a6458;
    --photo-light: #97a093;
    --photo-skin: #b38a74;
  }
  html, body {
    margin: 0;
    padding: 0;
    overflow: hidden;
    background: var(--paper);
  }
  .cover {
    position: relative;
    width: 1200px;
    height: 750px;
    overflow: hidden;
    background: var(--paper);
    font-family: "Questrial", "Century Gothic", sans-serif;
  }
  .cover-shapes {
    position: absolute;
    inset: 0;
    display: block;
  }
  .front-title {
    position: absolute;
    left: 47px;
    top: 99px;
    margin: 0;
    font-weight: 400;
    font-size: 21px;
    line-height: 26.5px;
    color: var(--paper);
  }
  .university {
    position: absolute;
    left: 396px;
    top: 10px;
    width: 163px;
    text-align: center;
  }
  .university-mark {
    display: block;
    width: 60px;
    height: 60px;
    margin: 0 auto;
    border-radius: 50%;
    border: 2px solid var(--ink);
    box-sizing: border-box;
  }
  .university-rule {
    height: 1px;
    background: #9a9a9a;
    margin: 12px 0 6px;
  }
  .university-name {
    font-family: "Roboto", "Arial", sans-serif;
    font-weight: 700;
    font-size: 12.5px;
    color: var(--ink);
    white-space: nowrap;
    letter-spacing: -0.2px;
  }
  .author-band {
    position: absolute;
    left: 58px;
    top: 699px;
    margin: 0;
    font-weight: 400;
    font-size: 27px;
    line-height: 37px;
    color: var(--paper);
  }
  .back-bio {
    position: absolute;
    left: 663px;
    top: 558px;
    width: 490px;
    margin: 0;
    font-size: 11.3px;
    line-height: 15px;
    color: var(--paper);
    text-align: center;
  }
</style>
</head>
<body>
<main class="cover">
  <svg class="cover-shapes" width="1200" height="750" viewBox="0 0 1600 1000" aria-hidden="false">
    <defs>
      <linearGradient id="photoTone" x1="0" y1="0" x2="1" y2="1">
        <stop offset="0" stop-color="var(--photo-light)" style="stop-color:#97a093"/>
        <stop offset="0.55" stop-color="#6f786b"/>
        <stop offset="0.75" stop-color="#b38a74"/>
        <stop offset="1" stop-color="#5a6458"/>
      </linearGradient>
    </defs>

    <!-- Front cover -->
    <rect class="front-photo" x="130" y="148" width="642" height="852" fill="url(#photoTone)"
          role="img" aria-label="Fotografía: un ojo que mira a través de un papel gris rasgado"/>
    <polygon class="front-slate" points="0,0 415,0 580,245 205,470 130,640 0,880" fill="#646a61"/>
    <polygon class="front-crimson-wedge" points="0,885 65,755 65,1000 0,1000" fill="#a51d3d"/>
    <rect class="front-name-band" x="65" y="915" width="338" height="85" fill="#a51d3d"/>

    <!-- Back cover -->
    <rect class="back-slate" x="830" y="0" width="770" height="1000" fill="#646a61"/>
    <polygon class="back-white-top" points="830,0 1505,0 1065,210 1050,210" fill="#ffffff"/>
    <polygon class="back-crimson" points="1505,0 1600,0 1600,30 1385,515 1383,525 1050,525 1050,208 1070,208" fill="#a51d3d"/>
    <polygon class="back-white-side" points="1600,30 1385,515 1600,730" fill="#ffffff"/>
    <rect class="portrait-slot" x="1060" y="218" width="313" height="300" fill="#ffffff"/>
  </svg>

  <h1 class="front-title">"Diseño, desarrollo y validación<br>de una encuesta para evaluar<br>el compromiso visual y emocional<br>subjetivos en pacientes<br>&nbsp;con Queratocono"</h1>

  <div class="university">
    <span class="university-mark"></span>
    <div class="university-rule"></div>
    <div class="university-name">Universidad de Montebrisa</div>
  </div>

  <p class="author-band">Iñigo Tarrasco</p>

  <p class="back-bio">"Iñigo Tarrasco, MD, es un Oftalmólogo Subespecialista en Cirugía Refractiva de la Universidad Serrana Metropolitana (Colombia) y la Universidad de Montebrisa (España). Actualmente se desempeña como miembro del Departamento de Córnea y Cirugía Refractiva de la Clínica de Oftalmología Vallealto y como director de su propia compañía de emprendimiento médico Silver Heron Surgical"</p>
</main>
</body>
</html>
```